Business Card design for an International Import Export House

We need a Business Card design for our import export business. We trade in Minerals, Metals, Rice, Sugar, Steel etc.. The design should be minimalistic. It may or may not contain the physical address. In case you want to include the physical address - 418 Verandah Heights, Marlow Sector 9, Ashvale, Korvanta, India, 408152.

Target Market(s)

Steel Mills or Steel Plants, Factories, Mining businesses, Industrial houses, Government Agencies

Industry/Entity Type

Importer

Contact Information for Business Card

Business Name - Tessan Overseas

Font styles to use
Other font styles liked:
• montserrat

Requirements
Must have
• Ravi Kandola - President
• www.tessanoverseas.com
• ravi@tessanoverseas.com
• +91-987-654-3217
Nice to have
• worldwide suppliers of ores

```html
<!DOCTYPE html>
<html lang="en">
<head>
<meta charset="utf-8">
<title>Tessan Overseas — Business Card</title>
<link rel="stylesheet" href="https://fonts.googleapis.com/css2?family=Montserrat:wght@400;500;600;700;800&display=swap">
<style>
  :root {
    --bg: #e9e7e2;
    --card-black: #0b0b0c;
    --accent: #3c9cb8;
    --accent-bright: #1e9fe0;
    --text-light: #f2f2f2;
    --text-muted: #c9c9c9;
  }
  * { box-sizing: border-box; margin: 0; padding: 0; }
  html, body {
    width: 1200px; height: 800px; overflow: hidden;
    background: var(--bg);
    font-family: "Montserrat", sans-serif;
  }
  .stage {
    width: 1200px; height: 800px;
    display: flex; align-items: center; justify-content: center; gap: 60px;
  }
  .card {
    position: relative;
    width: 525px; height: 300px;
    background: var(--accent);
    border-radius: 4px;
    overflow: hidden;
    box-shadow: 0 10px 30px rgba(0,0,0,0.18);
  }
  .card__panel {
    position: absolute;
    background: var(--card-black);
  }
  .card--front .card__panel {
    left: 0; top: 0; right: 22px; bottom: 22px;
    border-bottom-right-radius: 34px;
  }
  .card--back .card__panel {
    left: 22px; top: 0; right: 0; bottom: 22px;
    border-bottom-left-radius: 34px;
  }

  .brand {
    position: absolute;
    display: flex; align-items: center; gap: 9px;
  }
  .brand__dot {
    width: 14px; height: 14px; border-radius: 50%;
    background: var(--accent);
  }
  .brand__name {
    color: var(--accent);
    font-weight: 700;
    letter-spacing: 0.02em;
    text-transform: uppercase;
    white-space: nowrap;
  }
  .card--front .brand { top: 46px; right: 52px; }
  .card--front .brand__name { font-size: 15px; }
  .card--back .brand { left: 50%; top: 50%; transform: translate(-44%, -50%); }
  .card--back .brand__dot { width: 20px; height: 20px; }
  .card--back .brand__name { font-size: 22px; }

  .person { position: absolute; left: 40px; top: 100px; }
  .person__name {
    color: var(--text-light);
    font-size: 22px; font-weight: 800;
    letter-spacing: 0.02em; text-transform: uppercase;
    white-space: nowrap;
  }
  .person__title {
    color: var(--accent);
    font-size: 11px; font-weight: 500;
    letter-spacing: 0.08em; text-transform: uppercase;
    text-align: right; margin-top: 1px;
  }

  .contacts {
    position: absolute; left: 40px; top: 172px;
    display: grid; grid-template-columns: 170px 230px; column-gap: 14px; row-gap: 7px;
  }
  .contacts__col { display: flex; flex-direction: column; gap: 7px; }
  .contacts__col--wide { grid-column: 1 / span 2; }
  .contact {
    display: flex; align-items: flex-start; gap: 8px;
    color: var(--text-muted); font-size: 10.5px; line-height: 15px;
    white-space: nowrap;
  }
  .contact__icon {
    flex: none; width: 15px; height: 15px; border-radius: 3px;
    background: var(--accent-bright);
    display: flex; align-items: center; justify-content: center;
  }
  .contact__icon svg { width: 10px; height: 10px; fill: #fff; }
</style>
</head>
<body>
<main class="stage">

  <section class="card card--front" aria-label="Card front">
    <div class="card__panel"></div>

    <div class="brand">
      <span class="brand__dot"></span>
      <span class="brand__name">Tessan Overseas</span>
    </div>

    <div class="person">
      <h1 class="person__name">Ravi Kandola</h1>
      <p class="person__title">President</p>
    </div>

    <div class="contacts">
      <div class="contacts__col">
        <div class="contact">
          <span class="contact__icon"><svg viewBox="0 0 10 10"><path d="M2 1h2l1 2.2-1.2.8a5 5 0 0 0 2.2 2.2l.8-1.2L9 6v2a1 1 0 0 1-1 1A7 7 0 0 1 1 2a1 1 0 0 1 1-1z"/></svg></span>
          <span>+91-987-654-3217</span>
        </div>
        <div class="contact">
          <span class="contact__icon"><svg viewBox="0 0 10 10"><path d="M3 0.5h4a1 1 0 0 1 1 1v7a1 1 0 0 1-1 1H3a1 1 0 0 1-1-1v-7a1 1 0 0 1 1-1zm0 1.5v5.5h4V2z"/></svg></span>
          <span>+91-987-654-3217</span>
        </div>
      </div>
      <div class="contacts__col">
        <div class="contact">
          <span class="contact__icon"><svg viewBox="0 0 10 10"><path d="M5 .5a4.5 4.5 0 1 0 0 9 4.5 4.5 0 0 0 0-9zm0 1.2c.6.7 1 1.7 1.1 2.7H3.9C4 3.4 4.4 2.4 5 1.7zM3.9 5.6h2.2C6 6.6 5.6 7.6 5 8.3 4.4 7.6 4 6.6 3.9 5.6z"/></svg></span>
          <span>www.tessanoverseas.com</span>
        </div>
        <div class="contact">
          <span class="contact__icon"><svg viewBox="0 0 10 10"><path d="M1 2h8v6H1zm.9.8L5 5.2l3.1-2.4z"/></svg></span>
          <span>ravi@tessanoverseas.com</span>
        </div>
      </div>
      <div class="contacts__col contacts__col--wide">
        <div class="contact">
          <span class="contact__icon"><svg viewBox="0 0 10 10"><path d="M5 .5a3.2 3.2 0 0 0-3.2 3.2C1.8 6 5 9.5 5 9.5S8.2 6 8.2 3.7A3.2 3.2 0 0 0 5 .5zm0 2a1.2 1.2 0 1 1 0 2.4 1.2 1.2 0 0 1 0-2.4z"/></svg></span>
          <span>418 Verandah Heights, Marlow Sector 9, Ashvale,<br>Korvanta, India, 408152</span>
        </div>
      </div>
    </div>
  </section>

  <section class="card card--back" aria-label="Card back">
    <div class="card__panel"></div>
    <div class="brand">
      <span class="brand__dot"></span>
      <span class="brand__name">Tessan Overseas</span>
    </div>
  </section>

</main>
</body>
</html>
```